Vantora - High End Woman's Retail Store Flyer Design Project

Objective

Design a high impact elegant and classy flyer for distribution at mall entrances, homes etc. by promoters. The intent will be for the Target Audiencce to retain the flyer beyond just a cursory glance.

Format & Size

We are looking for two versions,

a) A5 size Double Sided printing
b) A4 size Four Sided printing

Overall Look & Feel

The creative suggested should align with the logo - its subtle yet distinctive style. The colours used would be a good reference to the kind of contrast colours we would like used for the Flyers as well. The flyer must stand out from the scores of flyers received each day by Coonsumers

Target Audience

- Woman in he age group of 20 - 50 yrs
- Literate, Outgoing, Social
- Urban, travelled internationally
- English speaking

Description of Business

We are a high end retail store targeted at woman. The store is located in North India in a high end mall. The store offers Cosmetics, Lingerie, Herbals, Fashion Jewelry, Fabric & Readymades. We offer an uncluttered highly sophisticated environment for consumers to shop at leisure.

The store is bright and features fresh flowers (Lilies) to make it more welcoming.

Brands Carried

We carry the following brands by category,

a) Cosmetics - Corvanelle, Dusket, Firza, Numa & Q'Astrid
b) Lingerie - Pellow, Ostiva, Brindsey, Ulvika, Kestrow, Tamsord
c) Herbals - Velmorie, GXTP, Meherunnisa Qadri, Pravo, Calvismera, Dunverosa, Vostelle
d) Accessories - Plain Quarters, Tidy Mend

Social Networking

Prominent mention of the store's Chatterlane site encouraging Consumers to 'Like' us on CL

Store Address & Timings

The store address and business hours of operations must be prominently mentioned.

Photographs

Please use royalty free images from your own stock library to add to those uploaded. Else, if you recommend we buy high quality imaages, please let us know.

Logo Colors & Fonts

0/11/0/22; 12/23/3/39; 1/0/5/12; 0/0/0/36; 3/18/2/37; 0/20/0/37; 1/1/1/37; 0/20/20/60

Font used is Bodoni MT Condensed
Updates

Hi,

Additonal notes for your consideration,

1) Please consider an option to include a tearable stub as part of the flyer design which would have space for the Consumer to provide their Name, Mobile Phone #, Address, Date of Birth, Chatterlane link as well as email alias 
2) Each tearable stub will be individually numbered (by the printer) so please asign a space for the same

Consumers will be entitled to a price off when thet walk in with the flyer.

Thanx!

Target Market(s)

Woman in age group 20 - 50 yrs

Industry/Entity Type

Environment

Requirements
Must have
• Brands Caarried
Store Address
Store Timings
Chatterlane Like Statement

```html
<!DOCTYPE html>
<html lang="en">
<head>
<meta charset="utf-8">
<title>Vantora – Store Flyer</title>
<link rel="stylesheet" href="https://fonts.googleapis.com/css2?family=Yanone+Kaffeesatz:wght@300;400&display=swap">
<style>
  :root {
    --trim-orange: #e8641e;
    --frame-grey: #c9c9c9;
    --paper-white: #ffffff;
    --stone-grey: #e4e3e1;
    --ink-brown: #3f3530;
    --soft-taupe: #a59a93;
    --logo-taupe: #6f6259;
    --band-mist: #eef1f3;
    --cut-red: #d9675a;
  }
  * { margin: 0; padding: 0; box-sizing: border-box; }
  html, body { width: 1200px; height: 853px; overflow: hidden; background: var(--frame-grey); }
  body { font-family: "Yanone Kaffeesatz", "Arial Narrow", sans-serif; color: var(--ink-brown); }

  .sheet { position: relative; width: 1200px; height: 853px; border: 6px solid var(--trim-orange); background: var(--frame-grey); }
  .spread { position: absolute; left: 6px; top: 6px; width: 1156px; height: 796px; overflow: hidden; }
  .spread-bg { position: absolute; left: 0; top: 0; }

  .photo { position: absolute; }
  .photo--powder {
    left: 420px; top: 10px; width: 360px; height: 270px;
    background: radial-gradient(ellipse 50% 50% at 50% 45%, rgba(214,52,94,.85) 0%, rgba(229,111,122,.7) 30%, rgba(240,179,166,.5) 60%, rgba(255,255,255,0) 100%);
  }
  .photo--model {
    left: 48px; top: 292px; width: 122px; height: 176px; border-radius: 48px 48px 0 0;
    background: linear-gradient(180deg, #6b4536 0%, #d7ad96 40%, #5b3458 72%, #d7ad96 100%);
  }
  .photo--cosmetics {
    left: 650px; top: 236px; width: 470px; height: 240px;
    background: linear-gradient(90deg, #b98a72 0%, #eab8c0 25%, #d88b78 45%, #f1a9b6 65%, #e5b6a4 85%, #eeeeee 100%);
  }
  .photo--earring-gold { background: linear-gradient(180deg, #c3a664 0%, #a98893 50%, #f3f1ec 100%); border-radius: 24px 24px 30px 30px; }
  .photo--earring-silver { background: linear-gradient(180deg, #a8a593 0%, #c9c7bb 50%, #f2f1ec 100%); border-radius: 30px 30px 44px 44px; }
  .earring-l1 { left: 112px; top: 458px; width: 42px; height: 136px; }
  .earring-l2 { left: 434px; top: 466px; width: 42px; height: 136px; }
  .earring-r1 { left: 668px; top: 456px; width: 76px; height: 156px; }
  .earring-r2 { left: 1016px; top: 456px; width: 76px; height: 156px; }

  .stub-number { position: absolute; left: -20px; top: -30px; width: 132px; height: 110px; border-radius: 50%; background: var(--stone-grey); }
  .stub-number span { position: absolute; left: 53px; top: 59px; font-size: 14px; }

  .brand { position: absolute; }
  .brand-dot { position: absolute; left: 0; top: 8px; width: 46px; height: 46px; border-radius: 50%; background: var(--stone-grey); }
  .brand-name { position: absolute; left: 40px; top: 0; font-size: 54px; font-weight: 400; color: var(--logo-taupe); line-height: 1; letter-spacing: 1px; white-space: nowrap; }
  .brand--left { left: 170px; top: 78px; }
  .brand--right { left: 780px; top: 78px; }

  .stub-form { position: absolute; left: 150px; top: 296px; }
  .stub-row { display: flex; align-items: flex-end; height: 24px; }
  .stub-label { width: 100px; text-align: right; font-size: 10px; font-weight: 300; padding-right: 5px; }
  .stub-line { width: 172px; border-bottom: 1px solid var(--soft-taupe); height: 10px; }

  .line { position: absolute; text-align: center; white-space: nowrap; line-height: 1; }
  .fit { display: inline-block; transform: scaleX(var(--sx, 1)); transform-origin: 50% 50%; }
  .headline { font-weight: 400; }
  .address { font-size: 9px; letter-spacing: 4px; color: var(--soft-taupe); }
  .stars { font-size: 10px; letter-spacing: 8px; }
  .hours { font-weight: 300; }
  .offer { font-weight: 400; }
  .like { font-size: 9.5px; font-weight: 400; }
  .rule { position: absolute; border-top: 1px solid var(--soft-taupe); }

  .brand-band { position: absolute; left: 588px; top: 695px; width: 572px; height: 70px; background: var(--band-mist); padding-top: 8px; }
  .brand-row { display: flex; height: 14px; align-items: center; }
  .brand-cat { width: 208px; text-align: right; font-size: 11.5px; padding-right: 10px; }
  .brand-list { font-size: 9px; letter-spacing: .3px; }

  .dims { position: absolute; left: 0; top: 0; pointer-events: none; }
  .dim-label { position: absolute; font-size: 10px; font-family: Arial, sans-serif; color: #333; background: var(--frame-grey); padding: 0 1px; }
</style>
</head>
<body>
<main class="sheet">
  <section class="spread">
    <svg class="spread-bg" width="1156" height="796" viewBox="0 0 1156 796">
      <rect width="1156" height="796" fill="var(--paper-white)"/>
      <path d="M0 394 Q300 575 594 394 L594 796 L0 796 Z" fill="var(--stone-grey)"/>
      <line x1="594" y1="0" x2="594" y2="796" stroke="#888" stroke-width="1" stroke-dasharray="4 4"/>
    </svg>

    <div class="photo photo--powder" role="img" aria-label="Burst of pink and coral makeup powder"></div>
    <div class="photo photo--cosmetics" role="img" aria-label="Row of lipsticks, mascara, lip gloss and pencils"></div>

    <svg class="spread-bg" width="1156" height="796" viewBox="0 0 1156 796">
      <path d="M594 402 Q880 545 1156 406 L1156 796 L594 796 Z" fill="var(--stone-grey)"/>
      <path d="M594 402 Q880 545 1156 406" fill="none" stroke="var(--paper-white)" stroke-width="7"/>
      <path d="M0 394 Q300 575 594 394" fill="none" stroke="var(--cut-red)" stroke-width="1" stroke-dasharray="3 3"/>
    </svg>
    <div class="photo photo--model" role="img" aria-label="Woman modelling lingerie"></div>

    <div class="stub-number"><span>NUMBER:</span></div>

    <div class="brand brand--left"><span class="brand-dot"></span><span class="brand-name">VANTORA</span></div>
    <div class="brand brand--right"><span class="brand-dot"></span><span class="brand-name">VANTORA</span></div>

    <div class="stub-form">
      <div class="stub-row"><span class="stub-label">NAME:</span><span class="stub-line"></span></div>
      <div class="stub-row"><span class="stub-label">MOBILE NUMBER:</span><span class="stub-line"></span></div>
      <div class="stub-row"><span class="stub-label">ADDRESS:</span><span class="stub-line"></span></div>
      <div class="stub-row"><span class="stub-label">DATE OF BIRTH:</span><span class="stub-line"></span></div>
      <div class="stub-row"><span class="stub-label">CHATTERLANE LINK:</span><span class="stub-line"></span></div>
      <div class="stub-row"><span class="stub-label">EMAIL:</span><span class="stub-line"></span></div>
    </div>

    <div class="photo photo--earring-gold earring-l1" role="img" aria-label="Gold drop earring with pearl"></div>
    <div class="photo photo--earring-gold earring-l2" role="img" aria-label="Gold drop earring with pearl"></div>
    <div class="photo photo--earring-silver earring-r1" role="img" aria-label="Silver filigree earring with pearl"></div>
    <div class="photo photo--earring-silver earring-r2" role="img" aria-label="Silver filigree earring with pearl"></div>

    <!-- left panel copy, centred on x 300 -->
    <div class="line headline" style="left:150px;width:300px;top:523px;font-size:56px;"><span class="fit" style="--sx:.66">VISIT US TODAY!</span></div>
    <div class="rule" style="left:215px;width:170px;top:581px;"></div>
    <div class="line address" style="left:150px;width:300px;top:591px;">LUMEN ARCADE, SHOP 14</div>
    <div class="line stars" style="left:150px;width:300px;top:624px;">★★★★★★★★★</div>
    <div class="line hours" style="left:150px;width:300px;top:660px;font-size:22px;"><span class="fit" style="--sx:.78">IS OPEN FROM 8:00 AM TILL 7:00 PM</span></div>
    <div class="line offer" style="left:150px;width:300px;top:691px;font-size:56px;"><span class="fit" style="--sx:.68">GET THE FINNEST</span></div>
    <div class="line like" style="left:150px;width:300px;top:757px;">LIKE US ON OUR CHATTERLANE PAGE WWW.CHATTERLANE.COM/CLPAGE</div>

    <!-- right panel copy, centred on x 867 -->
    <div class="line headline" style="left:717px;width:300px;top:502px;font-size:42px;letter-spacing:2px;"><span class="fit" style="--sx:.86">VISIT US TODAY!</span></div>
    <div class="rule" style="left:759px;width:216px;top:544px;"></div>
    <div class="line address" style="left:717px;width:300px;top:560px;">LUMEN ARCADE, SHOP 14</div>
    <div class="line stars" style="left:717px;width:300px;top:593px;">★★★★★★★★★</div>
    <div class="line hours" style="left:717px;width:300px;top:615px;font-size:23px;"><span class="fit" style="--sx:.89">IS OPEN FROM 8:00 AM TILL 7:00 PM</span></div>
    <div class="line offer" style="left:717px;width:300px;top:642px;font-size:52px;"><span class="fit" style="--sx:.72">GET THE FINNEST</span></div>

    <div class="brand-band">
      <div class="brand-row"><span class="brand-cat">COSMETICS:</span><span class="brand-list">CORVANELLE – DUSKET – FIRZA – NUMA – Q'ASTRID</span></div>
      <div class="brand-row"><span class="brand-cat">LINGERIE:</span><span class="brand-list">PELLOW – OSTIVA – BRINDSEY – ULVIKA – KESTROW – TAMSORD</span></div>
      <div class="brand-row"><span class="brand-cat">HERBALS:</span><span class="brand-list">VELMORIE – GXTP – MEHERUNNISA QADRI – PRAVO – CALVISMERA – DUNVEROSA – VOSTELLE</span></div>
      <div class="brand-row"><span class="brand-cat">ACCESSORIES:</span><span class="brand-list">PLAIN QUARTERS – TIDY MEND</span></div>
    </div>
    <div class="line like" style="left:588px;width:572px;top:781px;">LIKE US ON OUR CHATTERLANE PAGE WWW.CHATTERLANE.COM/CLPAGE</div>
  </section>

  <svg class="dims" width="1188" height="841" viewBox="0 0 1188 841">
    <g stroke="#555" stroke-width="1" fill="none">
      <line x1="0" y1="809" x2="1160" y2="809"/>
      <line x1="0" y1="820" x2="1160" y2="820"/>
      <line x1="1177" y1="0" x2="1177" y2="800"/>
      <line x1="1162" y1="0" x2="1162" y2="802"/>
    </g>
  </svg>
  <span class="dim-label" style="left:558px;top:803px;">424mm</span>
  <span class="dim-label" style="left:558px;top:815px;">420mm</span>
  <span class="dim-label" style="left:1168px;top:410px;writing-mode:vertical-rl;transform:rotate(180deg);">297mm</span>
</main>
</body>
</html>
```